Upscale business cards needed for family business

We need professional business cards created for several family members. We are a family business holding company. We would like these relatively simple and straightforward, but also with a unique element to set them apart. Probably stick with neutral and simple colors - white, grey etc. We need space for the traditional elements, including name, title, address, email/phone number. And we will be creating several from this template so it needs to be template that is easy to switch information in and out of.

Industry/Entity Type

Business

Contact Information for Business Card

Please include the attached Marwood Capital logo.

Requirements
Must have
• The attached Marwood Capital logo.

```html
<!DOCTYPE html>
<html lang="en">
<head>
<meta charset="utf-8">
<title>Marwood Capital — Business Cards</title>
<link href="https://fonts.googleapis.com/css2?family=Arimo:wght@400;700&display=swap" rel="stylesheet">
<style>
  :root {
    --backdrop: #3b322e;
    --card: #141414;
    --card-edge: #1e1e1e;
    --ink: #e9e9e9;
    --ink-muted: #9a9a9a;
    --gold: #d29a2c;
    --rule: #8a8a8a;
  }
  * { box-sizing: border-box; margin: 0; padding: 0; }
  html, body {
    width: 1200px; height: 864px; overflow: hidden;
    background: var(--backdrop);
    font-family: "Arimo", Arial, sans-serif;
  }
  .sheet {
    position: relative; width: 1200px; height: 864px;
    display: flex; align-items: center; justify-content: center; gap: 60px;
  }
  .card {
    position: relative; width: 525px; height: 300px;
    background: var(--card);
    border: 1px solid var(--card-edge);
    box-shadow: 0 14px 30px rgba(0,0,0,.45);
    color: var(--ink);
  }
  .brand-name {
    font-size: 30px; font-weight: 400; letter-spacing: 2px;
    color: var(--ink); text-transform: uppercase; white-space: nowrap;
  }
  .brand-rule { height: 1px; background: var(--rule); opacity: .6; }

  /* Back */
  .card--back { display: flex; flex-direction: column; align-items: center; justify-content: center; }
  .card--back .brand-rule { width: 290px; margin: 12px 0 26px; }
  .website-line { font-size: 13px; letter-spacing: 3px; color: var(--ink-muted); }

  /* Front */
  .card--front { display: flex; align-items: center; }
  .front-brand {
    width: 62%; display: flex; flex-direction: column; align-items: center;
  }
  .front-brand .brand-name { font-size: 24px; }
  .front-brand .brand-rule { width: 240px; margin-top: 10px; }
  .divider { width: 1px; height: 150px; background: var(--rule); opacity: .7; }
  .contact { padding-left: 18px; font-size: 13px; line-height: 1.35; }
  .contact__name { color: var(--gold); font-weight: 700; font-size: 16px; }
  .contact__title { margin-bottom: 8px; }
  .contact__address { margin-bottom: 8px; }
  .contact__row { display: flex; align-items: center; gap: 8px; }
  .contact__row svg { width: 12px; height: 12px; fill: var(--gold); flex: none; }
</style>
</head>
<body>
<main class="sheet">
  <section class="card card--back" aria-label="Card back">
    <div class="brand-name">Marwood Capital</div>
    <div class="brand-rule"></div>
    <div class="website-line">www.marwoodcapitalinc.com</div>
  </section>

  <section class="card card--front" aria-label="Card front">
    <div class="front-brand">
      <div class="brand-name">Marwood Capital</div>
      <div class="brand-rule"></div>
    </div>
    <div class="divider"></div>
    <div class="contact">
      <div class="contact__name">Elliot Marsh</div>
      <div class="contact__title">President</div>
      <div class="contact__address">2170 Alder Crescent<br>Brookvale, NY 11502</div>
      <div class="contact__row">
        <svg viewBox="0 0 12 12" aria-hidden="true"><path d="M2.5 1l2 2.2-1 1.3c.7 1.5 1.8 2.6 3.2 3.3l1.3-1 2.2 2L9.5 11C5 10.5 1.5 7 1 2.5z"/></svg>
        <span>518 3920 4471</span>
      </div>
      <div class="contact__row">
        <svg viewBox="0 0 12 12" aria-hidden="true"><path d="M1 3h10v6H1z M1 3l5 3.5L11 3" stroke="#141414" stroke-width=".8"/></svg>
        <span>elliot@marwoodcap.com</span>
      </div>
      <div class="contact__row">
        <svg viewBox="0 0 12 12" aria-hidden="true"><circle cx="6" cy="6" r="5"/><path d="M1 6h10M6 1c2 2.5 2 7.5 0 10M6 1c-2 2.5-2 7.5 0 10" stroke="#141414" stroke-width=".7" fill="none"/></svg>
        <span>www.marwoodcap.com</span>
      </div>
    </div>
  </section>
</main>
</body>
</html>
```